Business Cards

Need a neat design for a new business card

Industry/Entity Type

Residential Construction

Contact Information for Business Card

Company Name- KOVE Construction Inc.
Owner- Marcus Tolliver
Phone number- (555)203-7481
Email- kovecohomes@brindlemail.example
Facebook- www.socialpage.example/kovecohomes

Colors
fefdec

```html
<!DOCTYPE html>
<html lang="en">
<head>
<meta charset="utf-8">
<title>KOVE Construction – Business Card</title>
<link href="https://fonts.googleapis.com/css2?family=Arimo:wght@400;700&display=swap" rel="stylesheet">
<style>
  :root {
    --page: #fefdec;
    --ink: #08090b;
    --paper: #ffffff;
  }
  * { margin: 0; padding: 0; box-sizing: border-box; }
  html, body { width: 1169px; height: 1200px; overflow: hidden; }
  body {
    position: relative;
    background: var(--page);
    font-family: "Arimo", Arial, sans-serif;
    color: var(--ink);
  }
  .card {
    position: absolute;
    left: 154px;
    width: 861px;
    height: 492px;
  }
  .card--front { top: 93px; background: var(--ink); }
  .card--back { top: 617px; height: 490px; background: var(--paper); overflow: hidden; }

  .brand {
    position: absolute;
    display: flex;
    align-items: center;
    gap: 14px;
    font-weight: 700;
    letter-spacing: 3px;
    white-space: nowrap;
  }
  .brand__square { width: 18px; height: 18px; flex: none; }
  .card--front .brand {
    left: 50%; top: 50%;
    transform: translate(-50%, -50%);
    font-size: 30px;
    color: var(--paper);
  }
  .card--front .brand__square { background: var(--paper); }
  .card--back .brand {
    left: 679px; top: 245px;
    transform: translate(-50%, -50%);
    font-size: 25px;
    color: var(--ink);
  }
  .card--back .brand__square { background: var(--ink); width: 15px; height: 15px; }

  .person { position: absolute; left: 31px; top: 195px; }
  .person__name { font-size: 36px; font-weight: 400; line-height: 1; }
  .person__role { font-size: 24px; margin-top: 12px; line-height: 1; }

  .contact { position: absolute; left: 31px; top: 352px; list-style: none; }
  .contact__item {
    display: flex; align-items: center;
    height: 30px; margin-bottom: 15px;
    font-size: 22px;
  }
  .contact__icon { width: 32px; height: 28px; margin-right: 29px; flex: none; }

  .band { position: absolute; }
  .band--left { left: 0; top: 460px; width: 439px; height: 30px; }
  .band--right { left: 444px; top: 430px; width: 417px; height: 60px; }
  .band__url {
    position: absolute; left: 474px; top: 446px;
    font-size: 21px; color: var(--paper); white-space: nowrap;
  }
</style>
</head>
<body>

<section class="card card--front">
  <div class="brand"><span class="brand__square"></span>KOVE CONSTRUCTION</div>
</section>

<section class="card card--back">
  <div class="person">
    <h1 class="person__name">Marcus Tolliver</h1>
    <p class="person__role">Owner</p>
  </div>

  <ul class="contact">
    <li class="contact__item">
      <svg class="contact__icon" viewBox="0 0 32 28" aria-hidden="true">
        <path fill="#08090b" d="M5 2c1.5-1 3-1 4 .5l3 4.5c.8 1.3.4 2.6-.7 3.4l-1.6 1.2c1.6 3.5 4.3 6.3 7.8 8l1.3-1.5c.9-1 2.2-1.3 3.4-.5l4.4 3c1.4 1 1.5 2.5.5 3.8l-1.4 1.8c-1.5 1.8-4 2-6.5 1C11 24 4.5 17.6 1.8 10.3.8 7.7 1.5 4.8 3.4 3.3z"/>
      </svg>
      <span>(555)203-7481</span>
    </li>
    <li class="contact__item">
      <svg class="contact__icon" viewBox="0 0 32 28" aria-hidden="true">
        <rect x="1" y="4" width="30" height="21" fill="#08090b"/>
        <path d="M3 6l13 10L29 6M3 23l10-8M29 23l-10-8" fill="none" stroke="#fff" stroke-width="2"/>
      </svg>
      <span>kovecohomes@brindlemail.example</span>
    </li>
  </ul>

  <svg class="band band--left" viewBox="0 0 439 30" aria-hidden="true">
    <polygon points="0,0 439,0 432,30 0,30" fill="#08090b"/>
  </svg>
  <svg class="band band--right" viewBox="0 0 417 60" aria-hidden="true">
    <polygon points="14,0 417,0 417,60 0,60" fill="#08090b"/>
  </svg>
  <span class="band__url">www.socialpage.example/kovecohomes</span>

  <div class="brand"><span class="brand__square"></span>KOVE CONSTRUCTION</div>
</section>

</body>
</html>
```